Business Card Design Project

Use our current logo. Clean design.

Industry/Entity Type

Business

Requirements
Must have
• Marisela DUBRANCQ
M. Law
Managing Partner

Alpenvorsa AG
Kornhalmweg 214
CH-3097 Liebefeld

M. +41 79 412 56 27
T. +41 31 928 44 10
F. +41 31 928 44 19

m.dubrancq@alpenvorsa-example.com
www.alpenvorsa-example.com

```html
<!DOCTYPE html>
<html lang="en">
<head>
<meta charset="utf-8">
<title>Alpenvorsa AG – Business Card</title>
<link rel="stylesheet" href="https://fonts.googleapis.com/css2?family=Jost:wght@400;500&display=swap">
<style>
  :root {
    --brand-red: #bd1622;
    --brand-red-mark: #d4232f;
    --card-white: #ffffff;
    --ink: #1f1f1f;
    --ink-soft: #6f6f6f;
    --tab-grey: #8a8a8a;
    --backdrop: #e9e7e4;
  }
  * { margin: 0; padding: 0; box-sizing: border-box; }
  html, body {
    width: 1200px;
    height: 900px;
    overflow: hidden;
    background: var(--backdrop);
    font-family: "Jost", "Futura", sans-serif;
  }
  .canvas { position: relative; width: 1200px; height: 900px; }

  .card {
    position: absolute;
    width: 620px;
    height: 354px;
    overflow: hidden;
    box-shadow: 0 6px 18px rgba(0,0,0,0.12);
  }

  /* Back side: red */
  .card-back { left: 80px; top: 80px; background: var(--brand-red); }
  .brand-name {
    position: absolute;
    right: 34px;
    bottom: 30px;
    font-size: 40px;
    font-weight: 400;
    letter-spacing: 1px;
    color: var(--brand-red-mark);
  }

  /* Front side: white */
  .card-front { left: 500px; top: 466px; background: var(--card-white); }

  .email-tab {
    position: absolute;
    left: 0; top: 0;
    width: max-content;
    height: 42px;
    background: var(--brand-red);
    border-top-right-radius: 22px;
    color: var(--card-white);
    font-size: 16px;
    letter-spacing: 0.6px;
    text-transform: uppercase;
    line-height: 42px;
    padding: 0 30px 0 22px;
    white-space: nowrap;
  }

  .divider {
    position: absolute;
    left: 330px;
    top: 72px;
    width: 2px;
    height: 204px;
    background: var(--brand-red);
  }

  .identity {
    position: absolute;
    right: 304px;
    top: 134px;
    text-align: right;
    color: var(--ink);
    text-transform: uppercase;
    white-space: nowrap;
  }
  .identity .person-name { font-size: 25px; font-weight: 500; letter-spacing: 0.8px; line-height: 1.15; }
  .identity .person-title { font-size: 16px; letter-spacing: 0.5px; line-height: 1.3; }

  .contact {
    position: absolute;
    left: 346px;
    top: 76px;
    color: var(--ink-soft);
    font-size: 12.5px;
    letter-spacing: 0.6px;
    line-height: 1.35;
    text-transform: uppercase;
    white-space: nowrap;
  }
  .contact .address { margin-bottom: 18px; }

  .web-tab {
    position: absolute;
    right: 0; bottom: 28px;
    width: 240px;
    height: 30px;
    background: var(--tab-grey);
    border-top-left-radius: 16px;
    border-bottom-left-radius: 16px;
    color: var(--card-white);
    font-size: 11px;
    letter-spacing: 0.4px;
    line-height: 30px;
    text-align: right;
    padding-right: 12px;
    text-transform: uppercase;
    white-space: nowrap;
  }
</style>
</head>
<body>
  <main class="canvas">
    <section class="card card-back" aria-label="Card back">
      <div class="brand-name">Alpenvorsa</div>
    </section>

    <section class="card card-front" aria-label="Card front">
      <div class="email-tab">m.dubrancq@alpenvorsa-example.com</div>

      <div class="identity">
        <div class="person-name">Marisela Dubrancq</div>
        <div class="person-title">M.Law</div>
        <div class="person-title">Managing Partner</div>
      </div>

      <div class="divider"></div>

      <div class="contact">
        <div class="address">
          Alpenvorsa AG<br>
          Kornhalmweg 214<br>
          CH-3097 Liebefeld
        </div>
        <div class="numbers">
          M. +41 79 412 56 27<br>
          T. +41 31 928 44 10<br>
          F. +41 31 928 44 19
        </div>
      </div>

      <div class="web-tab">www.alpenvorsa-example.com</div>
    </section>
  </main>
</body>
</html>
```